Tri-fold flyer for Managed Services IT company

We need a tri-fold flyer design for our Managed Services IT company. Our website is here: https://pelicanfjordit.net. While we don't have to match our website we do want to incorporate the logo in the flyer. We would like a flyer that is *very* easy and quick to read/skim over and convey our message. Something like these:

https://www.artkestrel.com/design/58203917

https://47sketchyard.com/postcard-flyer-design/contests/create-lead-generating-flyer-postcard-managed-services-company-815243

http://www.marbleoaksystems.com/managed-services-no-cost-one-month/

Target Market(s)

Business to business IT services

Industry/Entity Type

It Service

Font styles to use
Serif
Sans Serif

Requirements
Must have
• *very* easy and quick to read/skim over and convey our message
Should not have
• verbose, lots of text

```html
<!DOCTYPE html>
<html lang="en">
<head>
<meta charset="utf-8">
<title>Pelican Fjord – IT Solutions Tri-fold</title>
<link href="https://fonts.googleapis.com/css2?family=Montserrat:wght@400;500;600;700;800&display=swap" rel="stylesheet">
<style>
:root{
  --blue:#254c96;
  --navy:#1e3a78;
  --orange:#ec7a1c;
  --paper:#ffffff;
  --mist:#eceef2;
  --ink:#1e3a78;
  --stage:#f1f1f1;
}
*{box-sizing:border-box;margin:0;padding:0}
html,body{width:876px;height:1200px;overflow:hidden}
body{background:var(--stage);font-family:"Montserrat",sans-serif;color:var(--ink);position:relative}

/* ---------- inside spread ---------- */
.spread{position:absolute;left:18px;top:20px;width:840px;height:560px;display:flex;background:var(--paper);box-shadow:0 2px 8px rgba(0,0,0,.12)}
.panel{position:relative;width:280px;height:560px;overflow:hidden;background:var(--mist)}
.panel + .panel{border-left:1px solid rgba(0,0,0,.06)}

.head-edge,.head{position:absolute;left:0;width:100%;clip-path:polygon(0 0,100% 0,100% 100%,57% 100%,50% calc(100% + 0px),50% 100%,0 100%)}
.head-edge{top:0;height:124px;background:var(--orange);clip-path:polygon(0 0,100% 0,100% 112px,56% 112px,50% 124px,44% 112px,0 112px)}
.head{top:0;height:120px;background:var(--blue);clip-path:polygon(0 0,100% 0,100% 108px,56% 108px,50% 120px,44% 108px,0 108px);z-index:2}
.panel.mid .head{background:var(--navy)}
.head .icon{position:absolute;left:50%;top:14px;width:42px;height:42px;margin-left:-21px;border-radius:50%;background:var(--paper);display:flex;align-items:center;justify-content:center}
.head .title{position:absolute;top:62px;width:100%;text-align:center;color:var(--paper);font-weight:800;font-size:19px;letter-spacing:.5px;line-height:1}
.head .sub{position:absolute;top:82px;width:100%;text-align:center;color:var(--orange);font-weight:600;font-size:13px;letter-spacing:1px}

.photo{position:absolute;left:0;top:0;width:100%;height:330px;background:linear-gradient(160deg,#d9d6d1 0%,#c9c5c0 40%,#e7e4e0 100%)}
.panel.mid .photo{background:linear-gradient(160deg,#cfcac4 0%,#b9b5b2 45%,#dedad5 100%)}
.panel.right .photo{background:linear-gradient(160deg,#e8d8cb 0%,#d9c3b3 40%,#efe6de 100%)}

.pitch{position:absolute;left:0;top:160px;width:100%;text-align:center;z-index:2;padding:0 22px}
.pitch .lead{font-size:14px;font-weight:500}
.pitch .big{font-size:19px;font-weight:800;line-height:1.15;margin:4px 0}
.pitch .tail{font-size:13px;font-weight:500;line-height:1.3}

.feat-band{position:absolute;left:0;top:330px;width:100%;height:38px;background:var(--blue);border-top:3px solid var(--orange);color:var(--paper);font-weight:800;font-size:15px;letter-spacing:.5px;display:flex;align-items:center;justify-content:center;z-index:2}
.panel.mid .feat-band{background:var(--navy);border-top-color:var(--orange)}
.features{position:absolute;left:0;top:368px;width:100%;bottom:0;list-style:none;padding:22px 20px 0 34px}
.panel.mid .features{background:var(--navy);color:var(--paper)}
.features li{position:relative;font-size:12.5px;font-weight:600;line-height:1.25;margin-bottom:9px;padding-left:16px}
.panel.left .features li{font-size:15px;font-weight:700;margin-bottom:10px}
.features li::before{content:"";position:absolute;left:0;top:3px;width:5px;height:9px;border:solid var(--orange);border-width:0 3px 3px 0;transform:rotate(40deg)}

/* ---------- front cover ---------- */
.cover{position:absolute;left:298px;top:610px;width:280px;height:560px;background:var(--paper);overflow:hidden;box-shadow:0 2px 8px rgba(0,0,0,.12)}
.cover .top-rule{position:absolute;left:0;top:0;width:100%;height:10px;background:var(--blue);border-bottom:3px solid var(--orange)}
.brand{position:absolute;top:52px;width:100%;display:flex;align-items:center;justify-content:center;gap:8px}
.brand .dot{width:12px;height:12px;border-radius:50%;background:var(--orange)}
.brand .name{font-weight:700;font-size:21px;letter-spacing:2px;color:var(--blue)}
.url-band{position:absolute;top:108px;left:38px;width:204px;height:22px;background:var(--blue);color:var(--paper);font-size:10px;font-weight:600;letter-spacing:1px;display:flex;align-items:center;justify-content:center}
.cover .photo{top:130px;height:210px;background:linear-gradient(150deg,#e9ecef 0%,#b7bfc9 45%,#5f6d80 75%,#d8dde3 100%)}
.slogan{position:absolute;left:0;top:318px;width:100%;height:86px;background:var(--blue);clip-path:polygon(0 26px,100% 0,100% 100%,0 100%);border-bottom:3px solid var(--orange);padding:34px 0 0 0;text-align:center}
.slogan .l1{color:var(--paper);font-weight:800;font-size:20px;line-height:1}
.slogan .l2{color:var(--orange);font-weight:800;font-size:18px;margin-top:4px}
.services{position:absolute;top:420px;width:100%;display:flex;justify-content:space-around;padding:0 8px}
.svc{width:84px;text-align:center}
.svc .ring{width:52px;height:52px;margin:0 auto 8px;border-radius:50%;background:var(--blue);border:3px solid var(--mist);box-shadow:0 0 0 2px var(--blue);display:flex;align-items:center;justify-content:center}
.svc .t{font-weight:800;font-size:11px;color:var(--blue);line-height:1.1}
.svc .s{font-weight:600;font-size:8px;color:var(--orange);letter-spacing:.5px}
.cover .foot{position:absolute;left:0;bottom:0;width:100%;height:20px;background:var(--navy);border-top:3px solid var(--orange)}
</style>
</head>
<body>

<section class="spread">
  <!-- Managed IT -->
  <article class="panel left">
    <div class="photo" role="img" aria-label="Soft office interior photograph"></div>
    <div class="head-edge"></div>
    <header class="head">
      <div class="icon"><svg width="24" height="22" viewBox="0 0 24 22"><rect x="2" y="2" width="20" height="13" rx="1.5" fill="none" stroke="#254c96" stroke-width="2.4"/><rect x="9" y="16" width="6" height="3" fill="#254c96"/><rect x="6" y="19" width="12" height="2" fill="#254c96"/></svg></div>
      <div class="title">MANAGED IT</div>
      <div class="sub">SERVICES</div>
    </header>
    <div class="pitch">
      <p class="lead">Strategically</p>
      <p class="big">OPTIMIZE AND<br>PROTECT</p>
      <p class="tail">your infrastructure with<br>24/7 proactive Monitoring.</p>
    </div>
    <div class="feat-band">FEATURES</div>
    <ul class="features">
      <li>Budget Your IT</li>
      <li>Reduce Costly Downtime</li>
      <li>Dependable Service</li>
    </ul>
  </article>

  <!-- Cloud IT -->
  <article class="panel mid">
    <div class="photo" role="img" aria-label="Photograph of hands typing on a laptop"></div>
    <div class="head-edge"></div>
    <header class="head">
      <div class="icon"><svg width="26" height="20" viewBox="0 0 26 20"><path d="M7 17h13a5 5 0 0 0 0-10 7 7 0 0 0-13-1A5.5 5.5 0 0 0 7 17z" fill="#1e3a78"/><path d="M13 15V8M10 11l3-3 3 3" stroke="#fff" stroke-width="2" fill="none"/></svg></div>
      <div class="title">CLOUD IT</div>
      <div class="sub">SERVICES</div>
    </header>
    <div class="pitch">
      <p class="lead">Cloud IT is the</p>
      <p class="big">FUTURE OF<br>SMALL &amp; MEDIUM</p>
      <p class="tail">business technology<br>management.</p>
    </div>
    <div class="feat-band">FEATURES</div>
    <ul class="features">
      <li>Hosted Larchpost Exchange</li>
      <li>Hosted Server Solutions</li>
      <li>Virtualized Desktop Solutions</li>
      <li>Hardware Virtualization</li>
      <li>Cloud Backup and Security</li>
      <li>Tidebin Storage for Business</li>
    </ul>
  </article>

  <!-- Security -->
  <article class="panel right">
    <div class="photo" role="img" aria-label="Close-up photograph of a hand on a keyboard"></div>
    <div class="head-edge"></div>
    <header class="head">
      <div class="icon"><svg width="20" height="24" viewBox="0 0 20 24"><path d="M5 11V7a5 5 0 0 1 10 0v4" stroke="#254c96" stroke-width="2.6" fill="none"/><rect x="2" y="10" width="16" height="12" rx="2" fill="#254c96"/><circle cx="10" cy="16" r="2" fill="#fff"/></svg></div>
      <div class="title">SECURITY</div>
      <div class="sub">SERVICES</div>
    </header>
    <div class="pitch">
      <p class="lead">Advanced security systems</p>
      <p class="big">HELP PROTECT<br>YOUR DATA</p>
      <p class="tail">and keep your business<br>up and running.</p>
    </div>
    <div class="feat-band">FEATURES</div>
    <ul class="features">
      <li>Unified Threat Management</li>
      <li>Web Filtering &amp; Firewall</li>
      <li>Spam Protection</li>
      <li>Digital Security Camera Systems</li>
      <li>Verrane Security Solutions</li>
      <li>Email Protection</li>
    </ul>
  </article>
</section>

<section class="cover">
  <div class="top-rule"></div>
  <div class="brand"><span class="dot"></span><span class="name">PELICAN FJORD</span></div>
  <div class="url-band">PELICANFJORDIT.NET</div>
  <div class="photo" role="img" aria-label="Photograph of three colleagues working together around a tablet"></div>
  <div class="slogan">
    <p class="l1">IT SOLUTIONS</p>
    <p class="l2">DESIGNED FOR YOU</p>
  </div>
  <div class="services">
    <div class="svc">
      <div class="ring"><svg width="24" height="22" viewBox="0 0 24 22"><rect x="2" y="2" width="20" height="13" rx="1.5" fill="none" stroke="#fff" stroke-width="2.4"/><rect x="9" y="16" width="6" height="3" fill="#fff"/><rect x="6" y="19" width="12" height="2" fill="#fff"/></svg></div>
      <div class="t">MANAGED IT</div><div class="s">SERVICES</div>
    </div>
    <div class="svc">
      <div class="ring"><svg width="26" height="20" viewBox="0 0 26 20"><path d="M7 17h13a5 5 0 0 0 0-10 7 7 0 0 0-13-1A5.5 5.5 0 0 0 7 17z" fill="#fff"/><path d="M13 15V8M10 11l3-3 3 3" stroke="#254c96" stroke-width="2" fill="none"/></svg></div>
      <div class="t">CLOUD IT</div><div class="s">SERVICES</div>
    </div>
    <div class="svc">
      <div class="ring"><svg width="20" height="24" viewBox="0 0 20 24"><path d="M5 11V7a5 5 0 0 1 10 0v4" stroke="#fff" stroke-width="2.6" fill="none"/><rect x="2" y="10" width="16" height="12" rx="2" fill="#fff"/><circle cx="10" cy="16" r="2" fill="#254c96"/></svg></div>
      <div class="t">SECURITY</div><div class="s">SERVICES</div>
    </div>
  </div>
  <div class="foot"></div>
</section>

</body>
</html>
```